Company identity deisgn should support 2 languages

I would like to get our company identity design
This includes the following only
Business Cards 2 languages Arabic and English
Email signature
Letterhead
Linkedin profile images
Attached is the logo in Ai format

Requirements
Must have
• For business card
Must have
Name and Adrees in arabic
Name and Address in english
You might use both side of the card
Should not have
• Any pictures other than the logo

```html
<!DOCTYPE html>
<html lang="en">
<head>
<meta charset="utf-8">
<title>Cognivo Systems — Stationery Set</title>
<link rel="stylesheet" href="https://fonts.googleapis.com/css2?family=Lato:wght@300;400;700&family=Open+Sans:wght@400;600;700&family=PT+Sans+Narrow:wght@700&family=Tajawal:wght@400;500;700&display=swap">
<style>
  :root {
    --brand-blue: #1b75bc;
    --brand-blue-deep: #1667a8;
    --ink: #3a3a3a;
    --ink-soft: #555;
    --rule: #c9c9c9;
    --band-grey: #d4d6d8;
    --paper: #ffffff;
  }
  * { box-sizing: border-box; margin: 0; padding: 0; }
  html, body { width: 1200px; height: 1020px; overflow: hidden; }
  body { background: var(--brand-blue); font-family: "Lato", sans-serif; color: var(--ink); position: relative; }

  .icon-defs { position: absolute; width: 0; height: 0; }

  /* Wordmark */
  .wordmark { display: flex; align-items: center; gap: 7px; color: var(--brand-blue); font-family: "Open Sans", sans-serif; font-weight: 600; letter-spacing: .08em; white-space: nowrap; }
  .wordmark-dot { border-radius: 50%; background: currentColor; flex: none; }

  /* Contact band */
  .contact-band { position: absolute; left: 0; right: 0; display: flex; }
  .contact-band-main { flex: 1; background: var(--brand-blue); color: #fff; display: flex; align-items: center; gap: 12px; font-family: "Open Sans", sans-serif; }
  .contact-band-end { background: var(--band-grey); }
  .contact-item { display: inline-flex; align-items: center; gap: 4px; white-space: nowrap; }
  .contact-item svg { fill: #fff; flex: none; }

  /* Letterhead */
  .letterhead { position: absolute; left: 40px; top: 95px; width: 640px; height: 829px; background: var(--paper); }
  .letterhead .wordmark { position: absolute; left: 57px; top: 43px; font-size: 15px; }
  .letterhead .wordmark-dot { width: 12px; height: 12px; }
  .letter-body { position: absolute; left: 68px; top: 180px; width: 505px; font-size: 10px; line-height: 13.8px; color: var(--ink-soft); font-weight: 300; }
  .letter-date { margin-bottom: 16px; font-weight: 400; }
  .letter-recipient { margin-bottom: 27px; font-weight: 400; }
  .letter-recipient strong { font-weight: 700; color: var(--ink); }
  .letter-salutation { margin-bottom: 14px; font-weight: 400; }
  .letter-body p.paragraph { text-align: justify; margin-bottom: 14px; }
  .letter-closing { margin-top: 28px; font-weight: 400; }
  .signature-area { margin-top: 6px; width: 205px; height: 26px; background: linear-gradient(90deg, #eef1f4, #f7f8fa); border-radius: 3px; }
  .letter-footer-rule { position: absolute; left: 57px; right: 57px; top: 741px; border-top: 1px solid var(--rule); }
  .letter-address { position: absolute; top: 756px; font-size: 10.5px; line-height: 12px; color: var(--ink); }
  .letter-address.en { left: 57px; }
  .letter-address.ar { right: 57px; direction: rtl; text-align: right; font-family: "Tajawal", sans-serif; font-size: 11px; }
  .letterhead .contact-band { top: 800px; height: 16px; }
  .letterhead .contact-band-main { padding-left: 57px; font-size: 10px; }
  .letterhead .contact-band-end { width: 95px; }

  /* Email signature */
  .email-signature { position: absolute; left: 700px; top: 160px; width: 460px; height: 114px; background: var(--paper); }
  .signature-headline { position: absolute; left: 26px; top: 24px; font-family: "PT Sans Narrow", sans-serif; font-weight: 700; font-size: 17px; color: var(--brand-blue); }
  .signature-tagline { position: absolute; left: 26px; top: 46px; width: 175px; font-family: "Open Sans", sans-serif; font-size: 7.4px; line-height: 9px; color: var(--brand-blue-deep); }
  .email-signature .wordmark { position: absolute; right: 34px; top: 42px; font-size: 12.5px; }
  .email-signature .wordmark-dot { width: 11px; height: 11px; }
  .email-signature .contact-band { top: 96px; height: 12px; }
  .email-signature .contact-band-main { justify-content: flex-end; padding-right: 10px; font-size: 7.3px; }
  .email-signature .contact-band-end { width: 60px; }

  /* Business cards */
  .business-card { position: absolute; left: 700px; width: 460px; height: 262px; border-radius: 14px; overflow: hidden; }
  .card-front { top: 304px; background: var(--paper); }
  .card-back { top: 596px; background: var(--brand-blue-deep); display: flex; align-items: center; justify-content: center; }
  .card-front .wordmark { position: absolute; left: 34px; top: 44px; font-size: 13px; }
  .card-front .wordmark-dot { width: 11px; height: 11px; }
  .card-back .wordmark { color: #fff; font-size: 19px; }
  .card-back .wordmark-dot { width: 16px; height: 16px; }
  .card-row { position: absolute; left: 34px; right: 34px; display: flex; justify-content: space-between; }
  .card-name-row { top: 124px; }
  .card-address-row { top: 176px; font-size: 10px; line-height: 13px; color: var(--ink); font-family: "Open Sans", sans-serif; }
  .card-rule { position: absolute; left: 34px; right: 34px; top: 164px; border-top: 1px solid var(--rule); }
  .card-name { font-family: "Open Sans", sans-serif; font-weight: 700; font-size: 14px; color: var(--brand-blue); line-height: 16px; }
  .card-title { font-family: "Open Sans", sans-serif; font-size: 10px; color: var(--ink); }
  .card-ar { direction: rtl; text-align: right; font-family: "Tajawal", sans-serif; }
  .card-ar .card-name { font-family: "Tajawal", sans-serif; font-size: 15px; }
  .card-ar .card-title, .card-address-row .card-ar { font-family: "Tajawal", sans-serif; font-size: 10.5px; }
  .card-front .contact-band { top: 228px; height: 16px; }
  .card-front .contact-band-main { padding-left: 24px; font-size: 9.3px; gap: 8px; }
  .card-front .contact-band-end { width: 70px; }
</style>
</head>
<body>

<svg class="icon-defs" aria-hidden="true">
  <symbol id="icon-phone" viewBox="0 0 16 16"><path d="M3.6 1.5l2.3 2.6-1.3 1.7c.9 2 2.6 3.7 4.6 4.6l1.7-1.3 2.6 2.3-1.4 2.4C6.7 13.4 2.6 9.3 1.2 2.9z"/></symbol>
  <symbol id="icon-mail" viewBox="0 0 16 16"><path d="M1 3.5h14v9H1zm1.6 1.2L8 8.6l5.4-3.9z"/></symbol>
  <symbol id="icon-globe" viewBox="0 0 16 16"><path d="M8 1a7 7 0 100 14A7 7 0 008 1zm0 1.5c.8.9 1.4 2.2 1.6 4H6.4C6.6 4.7 7.2 3.4 8 2.5zM5 6.5H2.7a5.5 5.5 0 013.1-3.6C5.4 3.8 5.1 5.1 5 6.5zm0 1.5c.1 1.4.4 2.7.8 3.6A5.5 5.5 0 012.7 8zm1.4 0h3.2c-.2 1.8-.8 3.1-1.6 4-.8-.9-1.4-2.2-1.6-4zm4.6 0h2.3a5.5 5.5 0 01-3.1 3.6c.4-.9.7-2.2.8-3.6zm0-1.5c-.1-1.4-.4-2.7-.8-3.6a5.5 5.5 0 013.1 3.6z"/></symbol>
</svg>

<!-- Letterhead -->
<section class="letterhead">
  <div class="wordmark"><span class="wordmark-dot"></span>COGNIVO SYSTEMS</div>

  <div class="letter-body">
    <p class="letter-date">01 January 2050</p>
    <p class="letter-recipient"><strong>Company (Pvt) Ltd.</strong><br>PO Box 3355 Mainville St<br>Sample City Country 3355</p>
    <p class="letter-salutation">Dear Oliver Brandt,</p>
    <p class="paragraph">Lorem ipsum dolor sit amet, consectetuer adipiscing elit, sed diam nonummy nibh euismod tincidunt ut laoreet dolore magna aliquam erat volutpat. Ut wisi enim ad minim veniam, quis nostrud exerci tation ullamcorper suscipit lobortis nisl ut aliquip ex ea commodo consequat. Duis dolore te feugait nulla facilisi. Nam liber tempor cum soluta nobis eleifend option congue nihil imperdiet doming id quod mazim placerat facer possim assum. Lorem ipsum dolor sit amet, consectetuer adipiscing elit, sed diam nonummy nibh euismod tincidunt ut laoreet dolore magna aliquam erat volutpat. Ut wisi enim ad minim veniam, quis nostrud exerci tation ullamcorper suscipit lobortis nisl ut aliquip ex ea commodo consequat.</p>
    <p class="paragraph">Consectetuer adipiscing elit, sed diam nonummy nibh euismod tincidunt ut laoreet dolore magna aliquam erat volutpat. Ut wisi enim ad minim veniam, quis nostrud exerci tation ullamcorper suscipit lobortis nisl ut aliquip ex ea commodo consequat. Consectetuer adipiscing elit, sed diam nonummy nibh euismod tincidunt ut laoreet dolore magna aliquam erat volutpat. Ut wisi enim ad minim veniam, quis nostrud exerci tation ullamcorper suscipit lobortis nisl ut aliquip ex ea commodo consequat.</p>
    <p class="paragraph">Consectetuer adipiscing elit, sed diam nonummy nibh euismod tincidunt ut laoreet dolore magna aliquam erat volutpat. Ut wisi enim ad minim veniam, quis nostrud exerci tation ullamcorper suscipit lobortis nisl ut aliquip ex ea commodo consequat. Consectetuer adipiscing elit, sed diam nonummy nibh euismod tincidunt ut laoreet dolore magna aliquam erat volutpat. Ut wisi enim ad minim veniam, quis nostrud exerci tation ullamcorper suscipit lobortis nisl ut aliquip ex ea commodo consequat.</p>
    <p class="letter-closing">Sincerely Yours</p>
    <div class="signature-area" role="img" aria-label="Handwritten signature of Daniel Roy Marston"></div>
  </div>

  <div class="letter-footer-rule"></div>
  <p class="letter-address en">Sahel Tower, 12<sup>th</sup> floor<br>Harbor Street,<br>Corniche District, Dammam 31411</p>
  <p class="letter-address ar">برج الساحل الدور 12<br>شارع الميناء<br>الكورنيش الدمام 31411</p>

  <div class="contact-band">
    <div class="contact-band-main">
      <span class="contact-item"><svg width="9" height="9"><use href="#icon-phone"/></svg>+96 4455 667 788</span>
      <span class="contact-item"><svg width="9" height="9"><use href="#icon-mail"/></svg>hello@cognivo.com</span>
      <span class="contact-item"><svg width="9" height="9"><use href="#icon-globe"/></svg>www.cognivo.com</span>
    </div>
    <div class="contact-band-end"></div>
  </div>
</section>

<!-- Email signature -->
<section class="email-signature">
  <h2 class="signature-headline">Cognivo Systems</h2>
  <p class="signature-tagline">From toothbrush to TV and cars to space technology, AI is everywhere and our expertise in AI will take you toward success.</p>
  <div class="wordmark"><span class="wordmark-dot"></span>COGNIVO SYSTEMS</div>
  <div class="contact-band">
    <div class="contact-band-main">
      <span class="contact-item"><svg width="7" height="7"><use href="#icon-phone"/></svg>+96 4455 667 788</span>
      <span class="contact-item"><svg width="7" height="7"><use href="#icon-mail"/></svg>hello@cognivo.com</span>
      <span class="contact-item"><svg width="7" height="7"><use href="#icon-globe"/></svg>www.cognivo.com</span>
    </div>
    <div class="contact-band-end"></div>
  </div>
</section>

<!-- Business card front -->
<section class="business-card card-front">
  <div class="wordmark"><span class="wordmark-dot"></span>COGNIVO SYSTEMS</div>
  <div class="card-row card-name-row">
    <div class="card-en">
      <p class="card-name">Khalid Alharbi</p>
      <p class="card-title">Business Development Director</p>
    </div>
    <div class="card-ar">
      <p class="card-name">خالد الحربي</p>
      <p class="card-title">مدير تطوير الأعمال</p>
    </div>
  </div>
  <div class="card-rule"></div>
  <div class="card-row card-address-row">
    <p class="card-en">Sahel Tower, 12<sup>th</sup> floor<br>Harbor Street<br>Corniche District, Dammam 31411</p>
    <p class="card-ar">برج الساحل الدور 12<br>شارع الميناء<br>الكورنيش الدمام 31411</p>
  </div>
  <div class="contact-band">
    <div class="contact-band-main">
      <span class="contact-item"><svg width="8" height="8"><use href="#icon-phone"/></svg>+96 4455 667 788</span>
      <span class="contact-item"><svg width="8" height="8"><use href="#icon-mail"/></svg>hello@cognivo.com</span>
      <span class="contact-item"><svg width="8" height="8"><use href="#icon-globe"/></svg>www.cognivo.com</span>
    </div>
    <div class="contact-band-end"></div>
  </div>
</section>

<!-- Business card back -->
<section class="business-card card-back">
  <div class="wordmark"><span class="wordmark-dot"></span>COGNIVO SYSTEMS</div>
</section>

</body>
</html>
```